Business card design needed

Double sided
Color, unique, elegant

Maybe put this quote somewhere?? But I think it might make it to cluttered?
“The Pilates Method of Body
Conditioning develops the body
uniformly, corrects posture, restores
vitality, invigorates the mind and
elevates the spirit”
- Henrik Dovacombe

Industry/Entity Type

Business

Contact Information for Business Card

Marta Kellbrook
Pilates Instructor & Personal trainer
Mobile: 0498265043
www.lorvix.com.au
email: lorvixhealth.fitness@qentamail.com

```html
<!DOCTYPE html>
<html lang="en">
<head>
<meta charset="utf-8">
<title>Marta Kellbrook Pilates – Business Card</title>
<link rel="stylesheet" href="https://fonts.googleapis.com/css2?family=Questrial&display=swap">
<style>
  :root {
    --backdrop: #1c1c1e;
    --card-white: #ffffff;
    --band-black: #0b0a0c;
    --band-sheen: #5a5a5e;
    --brand-pink: #ec008c;
    --brand-blue: #4a55b0;
    --quote-grey: #9a9a9a;
    --faint-grey: #e4e4e4;
    --contact-white: #f2f2f2;
  }
  * { box-sizing: border-box; margin: 0; padding: 0; }
  html, body {
    width: 1200px; height: 848px; overflow: hidden;
    background: var(--backdrop);
    font-family: "Questrial", "Century Gothic", sans-serif;
  }
  .card {
    position: absolute;
    width: 520px; height: 300px;
    background: var(--card-white);
    overflow: hidden;
    box-shadow: 0 14px 40px rgba(0,0,0,0.55);
  }
  .card--back { left: 60px; top: 274px; }
  .card--front { left: 620px; top: 274px; }

  .band {
    position: absolute; left: 0; right: 0;
    background: linear-gradient(to bottom, var(--band-sheen) 0, var(--band-black) 10px, var(--band-black) 100%);
  }
  .card--front .band { top: 184px; bottom: 0; }
  .card--back .band { top: 170px; height: 84px; }

  /* brand name mark */
  .brand { position: absolute; display: flex; align-items: center; gap: 8px; color: var(--brand-pink); }
  .brand__square { display: block; background: var(--brand-pink); }
  .card--front .brand { left: 26px; top: 24px; font-size: 24px; }
  .card--front .brand__square { width: 18px; height: 18px; }
  .brand--faint { right: 60px; top: 120px; color: var(--faint-grey); font-size: 34px; }
  .brand--faint .brand__square { width: 30px; height: 30px; background: var(--faint-grey); }
  .brand--small { right: 16px; bottom: 12px; font-size: 13px; gap: 5px; }
  .brand--small .brand__square { width: 11px; height: 11px; }

  /* front: identity */
  .identity { position: absolute; right: 24px; top: 128px; text-align: right; }
  .identity__name { color: var(--brand-pink); font-size: 22px; font-weight: 400; }
  .identity__role { color: var(--brand-blue); font-size: 11px; margin-top: 3px; }

  /* front: contacts */
  .contacts { position: absolute; left: 16px; top: 196px; list-style: none; }
  .contacts__row { display: flex; align-items: center; gap: 8px; height: 22px; color: var(--contact-white); font-size: 15px; }
  .contacts__key {
    width: 15px; height: 16px; background: var(--brand-pink); color: #fff;
    font-size: 12px; display: flex; align-items: center; justify-content: center;
  }

  /* back: quote */
  .quote { position: absolute; left: 30px; top: 18px; width: 270px; }
  .quote__mark { color: var(--quote-grey); font-size: 40px; line-height: 1; font-family: Georgia, serif; }
  .quote__mark--close { position: absolute; left: 240px; top: 128px; }
  .quote__text { color: var(--brand-blue); font-size: 11px; line-height: 1.35; margin-top: -8px; }
  .quote__author { color: var(--brand-pink); font-size: 18px; margin-top: 10px; }
</style>
</head>
<body>
  <section class="card card--back" aria-label="Card back">
    <div class="band"></div>
    <div class="brand brand--faint" aria-hidden="true"><span class="brand__square"></span>Lorvix</div>
    <blockquote class="quote">
      <div class="quote__mark">“</div>
      <p class="quote__text">The Pilates Method of Body Conditioning develops the body uniformly, corrects posture, restores vitality, invigorates the mind and elevates the spirit.</p>
      <p class="quote__author">- Henrik Dovacombe</p>
      <div class="quote__mark quote__mark--close">”</div>
    </blockquote>
    <div class="brand brand--small"><span class="brand__square"></span>Lorvix</div>
  </section>

  <section class="card card--front" aria-label="Card front">
    <div class="brand"><span class="brand__square"></span>Lorvix</div>
    <div class="identity">
      <h1 class="identity__name">Marta Kellbrook Pilates</h1>
      <p class="identity__role">Instructor &amp; Personal Trainer</p>
    </div>
    <div class="band"></div>
    <ul class="contacts">
      <li class="contacts__row"><span class="contacts__key">M</span>0498265043</li>
      <li class="contacts__row"><span class="contacts__key">W</span>lorvix.com.au</li>
      <li class="contacts__row"><span class="contacts__key">E</span>lorvixhealth.fitness@qentamail.com</li>
    </ul>
  </section>
</body>
</html>
```